Log In Screen Design

We have an existing website (www.velmarix4.com) and have recently developed software which requires a login screen using a similar theme from the velmarix4 website. The login screen should have a username and password. The software title is Tiered Outcome Scheduling (TOS). The VELMARIX4 log should appear on the login screen and the page should look professional.
Target Market(s)
Project Management Professionals
Industry/Entity Type
Software
Requirements
Must have
- Username and password blocks
Company Logo
Company Name - VELMARIX4 Management Ltd
Software Name - Tiered Outcome Scheduling (TOS)
Similar theme (colors) to the logo and existing website

```html
<!DOCTYPE html>
<html lang="en">
<head>
<meta charset="utf-8">
<title>VELMARIX4 – Tiered Outcome Scheduling Login States</title>
<link rel="stylesheet" href="https://fonts.googleapis.com/css2?family=Open+Sans:wght@400;600;700&display=swap">
<style>
  :root {
    --page-bg: #ffffff;
    --panel-bg: #efefef;
    --brand-blue: #3a78bf;
    --brand-blue-dark: #2e64a3;
    --link-blue: #2f7fd0;
    --text-grey: #5b5b5b;
    --logo-circle: #8a9db5;
    --field-border: #cfcfcf;
    --field-focus: #8fb8e6;
    --error-red: #d5443f;
    --muted: #6a6a6a;
  }
  html, body {
    margin: 0;
    padding: 0;
    width: 1200px;
    height: 445px;
    overflow: hidden;
    background: var(--page-bg);
    font-family: "Open Sans", Arial, sans-serif;
  }
  .stage {
    position: relative;
    width: 1060px;
    height: 393px;
    transform: scale(1.1321);
    transform-origin: 0 0;
  }
  .login-panel {
    position: absolute;
    top: 8px;
    background: var(--panel-bg);
    border-top: 7px solid var(--brand-blue);
    box-shadow: 0 2px 5px rgba(0,0,0,0.3);
    box-sizing: border-box;
  }
  .panel-default { left: 10px; width: 340px; height: 350px; }
  .panel-invalid { left: 362px; width: 346px; height: 374px; }
  .panel-failed  { left: 715px; width: 330px; height: 374px; }

  .brand {
    position: absolute;
    top: 18px;
    left: 18px;
    display: flex;
    align-items: center;
    gap: 16px;
  }
  .brand-mark {
    width: 62px;
    height: 62px;
    border-radius: 50%;
    background: var(--logo-circle);
    flex: none;
  }
  .brand-name {
    font-size: 21px;
    font-weight: 700;
    color: var(--text-grey);
    line-height: 1.2;
  }
  .app-title {
    position: absolute;
    top: 92px;
    left: 0;
    right: 0;
    margin: 0;
    text-align: center;
    font-size: 17px;
    font-weight: 700;
    color: var(--text-grey);
  }
  .field-label {
    position: absolute;
    width: 130px;
    text-align: right;
    font-size: 17px;
    font-weight: 700;
    color: var(--text-grey);
    line-height: 30px;
  }
  .field-input {
    position: absolute;
    width: 168px;
    height: 30px;
    box-sizing: border-box;
    background: #fff;
    border: 1px solid var(--field-border);
    border-radius: 6px;
    padding: 0 7px;
    font-size: 13px;
    line-height: 28px;
    color: #222;
  }
  .field-input.is-focused {
    border-color: var(--field-focus);
    box-shadow: 0 0 5px rgba(58,120,191,0.55);
  }
  .field-input.is-secret { font-size: 15px; font-weight: 700; letter-spacing: 0; }
  .error-pill {
    position: absolute;
    width: 278px;
    height: 19px;
    border-radius: 10px;
    background: var(--error-red);
    color: #fff;
    font-size: 12px;
    font-weight: 700;
    text-align: center;
    line-height: 19px;
  }
  .login-button {
    position: absolute;
    width: 85px;
    height: 36px;
    border-radius: 5px;
    background: var(--brand-blue);
    color: #fff;
    font-size: 17px;
    font-weight: 700;
    text-align: center;
    line-height: 36px;
    box-shadow: inset 0 -2px 0 var(--brand-blue-dark);
  }
  .forgot-link {
    position: absolute;
    left: 0;
    right: 0;
    text-align: center;
    font-size: 15px;
    font-weight: 700;
    color: var(--link-blue);
  }
  .copyright {
    position: absolute;
    left: 0;
    right: 0;
    text-align: center;
    font-size: 10px;
    color: var(--muted);
  }
</style>
</head>
<body>
<div class="stage">

  <section class="login-panel panel-default">
    <div class="brand"><span class="brand-mark"></span><span class="brand-name">VELMARIX4<br>Management Limited</span></div>
    <h1 class="app-title">Tiered Outcome Scheduling (TOS)</h1>
    <span class="field-label" style="left:0;top:147px">Username:</span>
    <div class="field-input" style="left:140px;top:147px">Daniel</div>
    <span class="field-label" style="left:0;top:188px">Password:</span>
    <div class="field-input is-focused is-secret" style="left:140px;top:188px">•••••••••</div>
    <div class="login-button" style="left:130px;top:245px">Login</div>
    <div class="forgot-link" style="top:298px">Forgot password?</div>
    <div class="copyright" style="top:326px">Copyright © 2013 www.velmarix4.com All rights reserved.</div>
  </section>

  <section class="login-panel panel-invalid">
    <div class="brand"><span class="brand-mark"></span><span class="brand-name">VELMARIX4<br>Management Limited</span></div>
    <h1 class="app-title">Tiered Outcome Scheduling (TOS)</h1>
    <span class="field-label" style="left:1px;top:147px">Username:</span>
    <div class="field-input" style="left:141px;top:147px">$£!@</div>
    <div class="error-pill" style="left:33px;top:186px">Username contains invalid characters</div>
    <span class="field-label" style="left:1px;top:215px">Password:</span>
    <div class="field-input is-focused is-secret" style="left:141px;top:215px">••••••••••</div>
    <div class="login-button" style="left:129px;top:271px">Login</div>
    <div class="forgot-link" style="top:324px">Forgot password?</div>
    <div class="copyright" style="top:351px">Copyright © 2013 www.velmarix4.com All rights reserved.</div>
  </section>

  <section class="login-panel panel-failed">
    <div class="brand"><span class="brand-mark"></span><span class="brand-name">VELMARIX4<br>Management Limited</span></div>
    <h1 class="app-title">Tiered Outcome Scheduling (TOS)</h1>
    <span class="field-label" style="left:-4px;top:145px">Username:</span>
    <div class="field-input" style="left:136px;top:145px"></div>
    <span class="field-label" style="left:-4px;top:186px">Password:</span>
    <div class="field-input" style="left:136px;top:186px"></div>
    <div class="error-pill" style="left:27px;top:226px">Username and/or Password Incorrect</div>
    <div class="login-button" style="left:124px;top:270px">Login</div>
    <div class="forgot-link" style="top:324px">Forgot password?</div>
    <div class="copyright" style="top:350px">Copyright © 2013 www.velmarix4.com All rights reserved.</div>
  </section>

</div>
</body>
</html>
```